The Tidy Lantern Business Card

I need a business card designed for The Tidy Lantern. The company provides on site support and education to end consumers in the ins and outs of all our digital devices. We advise on product purchase, installation, maintenance and troubleshooting. Anything from cordless phones to home networks.
My initial concept is double sided with the white logo on green on one side and contact details and a small logo on the flip side (logo package attached)
Contact Details:
Miles Fenwright
Managing Director
PO Box 43
Brackton, NSW 2187
Phone: 0438 907 516
email: miles@tidylantern.com.au
web: www.tidylantern.com.au
Target Market(s)
Busy professionals and retired folks.
Industry/Entity Type
Education
Look and feel

```html
<!DOCTYPE html>
<html lang="en">
<head>
<meta charset="utf-8">
<title>The Tidy Lantern — Business Card</title>
<link rel="stylesheet" href="https://fonts.googleapis.com/css2?family=Source+Sans+3:ital,wght@0,400;0,700;1,400&display=swap">
<style>
  :root {
    --backdrop-light: #f3f3f4;
    --backdrop-dark: #c3c4c6;
    --card-green: #80b23a;
    --card-green-light: #b9da62;
    --card-green-mid: #8fbf3f;
    --ink-navy: #13304a;
    --ink-green: #2f8a2f;
    --icon-fill: #eef5df;
    --white: #ffffff;
  }
  * { margin: 0; padding: 0; box-sizing: border-box; }
  html, body {
    width: 1200px;
    height: 1200px;
    overflow: hidden;
  }
  body {
    position: relative;
    background: radial-gradient(circle at 50% 45%, var(--backdrop-light) 0%, var(--backdrop-dark) 100%);
    font-family: "Source Sans 3", "Myriad Pro", Arial, sans-serif;
    color: var(--ink-navy);
  }
  .card {
    position: absolute;
    left: 218px;
    width: 765px;
    height: 461px;
  }
  .card--front {
    top: 130px;
    background: radial-gradient(ellipse 60% 65% at 62% 22%, var(--card-green-light) 0%, var(--card-green-mid) 60%, var(--card-green) 100%);
  }
  .card--back {
    top: 600px;
    background: var(--card-green);
  }

  /* Front side */
  .holder {
    position: absolute;
    left: 71px;
    top: 104px;
  }
  .holder__name {
    font-size: 21px;
    font-weight: 700;
    color: var(--ink-navy);
    line-height: 1.2;
  }
  .holder__title {
    font-size: 18px;
    font-style: italic;
    color: var(--ink-green);
    line-height: 1.3;
  }
  .brand-small {
    position: absolute;
    left: 430px;
    top: 50px;
    display: flex;
    align-items: center;
    gap: 12px;
  }
  .brand-small__dot {
    width: 40px;
    height: 40px;
    border-radius: 50%;
    background: var(--ink-green);
  }
  .brand-small__name {
    font-size: 32px;
    font-weight: 400;
    color: var(--ink-navy);
    white-space: nowrap;
  }
  .phone {
    position: absolute;
    left: 388px;
    top: 236px;
    display: flex;
    align-items: center;
    gap: 8px;
  }
  .phone__icon { width: 42px; height: 42px; }
  .phone__number {
    font-size: 44px;
    font-weight: 700;
    color: var(--ink-navy);
    letter-spacing: 0.5px;
    line-height: 1;
  }
  .contact-list {
    position: absolute;
    left: 42px;
    top: 357px;
    list-style: none;
  }
  .contact-list__item {
    display: flex;
    align-items: center;
    gap: 8px;
    font-size: 19px;
    line-height: 24.5px;
    color: var(--ink-navy);
  }
  .contact-list__icon { width: 18px; height: 18px; flex: none; }

  /* Back side */
  .brand-large {
    position: absolute;
    left: 60px;
    top: 0;
    height: 100%;
    display: flex;
    align-items: center;
    gap: 26px;
  }
  .brand-large__dot {
    width: 90px;
    height: 90px;
    border-radius: 50%;
    background: var(--white);
  }
  .brand-large__name {
    font-size: 78px;
    font-weight: 400;
    color: var(--white);
    white-space: nowrap;
    line-height: 1;
  }
</style>
</head>
<body>

  <section class="card card--front" aria-label="Business card front">
    <div class="holder">
      <p class="holder__name">Miles Fenwright</p>
      <p class="holder__title">Managing Director</p>
    </div>

    <div class="brand-small">
      <span class="brand-small__dot"></span>
      <span class="brand-small__name">The Tidy Lantern</span>
    </div>

    <div class="phone">
      <svg class="phone__icon" viewBox="0 0 42 42" aria-hidden="true">
        <circle cx="21" cy="21" r="20" fill="var(--ink-green)" opacity="0.85"/>
        <path d="M13 16c0-2 1.5-3.5 3-3.5l2 3-2 2c1 3 4 6 7 7l2-2 3 2c0 1.5-1.5 3-3.5 3C18 27.5 13 22 13 16z" fill="var(--white)"/>
      </svg>
      <span class="phone__number">0438 907 516</span>
    </div>

    <ul class="contact-list">
      <li class="contact-list__item">
        <svg class="contact-list__icon" viewBox="0 0 18 18" aria-hidden="true">
          <circle cx="9" cy="9" r="8.5" fill="var(--ink-navy)"/>
          <path d="M4.5 9.2 9 5l4.5 4.2h-1.3V13H10v-2.5H8V13H5.8V9.2z" fill="var(--icon-fill)"/>
        </svg>
        <span>PO Box 43 Brackton, NSW 2187</span>
      </li>
      <li class="contact-list__item">
        <svg class="contact-list__icon" viewBox="0 0 18 18" aria-hidden="true">
          <circle cx="9" cy="9" r="8.5" fill="var(--ink-navy)"/>
          <rect x="4.2" y="5.8" width="9.6" height="6.6" rx="0.8" fill="var(--icon-fill)"/>
          <path d="M4.5 6.2 9 9.6l4.5-3.4" fill="none" stroke="var(--ink-navy)" stroke-width="1"/>
        </svg>
        <span>miles@tidylantern.com.au</span>
      </li>
      <li class="contact-list__item">
        <svg class="contact-list__icon" viewBox="0 0 18 18" aria-hidden="true">
          <circle cx="9" cy="9" r="8.5" fill="var(--ink-navy)"/>
          <g fill="none" stroke="var(--icon-fill)" stroke-width="1">
            <circle cx="9" cy="9" r="5.2"/>
            <ellipse cx="9" cy="9" rx="2.3" ry="5.2"/>
            <path d="M3.8 9h10.4M4.6 6.3h8.8M4.6 11.7h8.8"/>
          </g>
        </svg>
        <span>www.tidylantern.com.au</span>
      </li>
    </ul>
  </section>

  <section class="card card--back" aria-label="Business card back">
    <div class="brand-large">
      <span class="brand-large__dot"></span>
      <span class="brand-large__name">The Tidy Lantern</span>
    </div>
  </section>

</body>
</html>
```